I work in creative/artistic projects across different mediums.
It needs to communicate creativity, style, sexy, uniqueness, individuality and sophistication.
It should not look corporate.
Colours I like are black silver gold deep purple, chocolate, orchid.
It doesn't have to make use of all these colours.
I do not like bright primary colors.
Updates

Project Deadline Extended
Reason: Still in the communication process and to allow the person enough time to finish the design. Though i should know in the next day or two. Thank you.

Target Market(s)

creatives and companies wanting to inject creativity into thier business.

Industry/Entity Type

Work

Contact Information for Business Card

Lionel Crowthwick
0418359026
lionel@lionelcrowthwick.com

quietsilverhour.com.au

Requirements
Should not have
• Anything corporate OR OLD FASHIONED

```html
<!DOCTYPE html>
<html lang="en">
<head>
<meta charset="utf-8">
<title>Lionel Crowthwick — Business Card</title>
<link href="https://fonts.googleapis.com/css2?family=Almendra&family=Arimo&display=swap" rel="stylesheet">
<style>
  :root {
    --page-bg: #d9d6d8;
    --card-frame: #2b2028;
    --plum-deep: #3f1738;
    --plum-mid: #521a4b;
    --plum-glow: #62185c;
    --name-band: #5f1c5a;
    --lilac: #cdb6cc;
    --lilac-soft: #b9a3b8;
  }
  * { box-sizing: border-box; margin: 0; padding: 0; }
  html, body { width: 1200px; height: 1000px; overflow: hidden; }
  body {
    background: var(--page-bg);
    display: flex;
    align-items: center;
    justify-content: center;
    font-family: "Arimo", Arial, sans-serif;
  }
  .business-card {
    position: relative;
    width: 1000px;
    height: 580px;
    background: var(--card-frame);
    padding: 14px;
    box-shadow: 0 18px 40px rgba(0,0,0,0.25);
  }
  .card-face {
    position: relative;
    width: 100%;
    height: 100%;
    background: radial-gradient(ellipse at 60% 30%, var(--plum-glow) 0%, var(--plum-mid) 45%, var(--plum-deep) 100%);
    overflow: hidden;
  }
  .name-band {
    position: absolute;
    top: 62px;
    right: 40px;
    background: var(--name-band);
    padding: 10px 26px 12px;
    font-family: "Almendra", serif;
    font-size: 46px;
    letter-spacing: 1px;
    color: var(--lilac);
  }
  .contact-list {
    position: absolute;
    top: 170px;
    left: 130px;
    list-style: none;
  }
  .contact-item {
    display: flex;
    align-items: center;
    height: 72px;
    font-size: 27px;
    color: var(--lilac);
  }
  .contact-icon {
    width: 40px;
    height: 40px;
    margin-right: 34px;
    flex: none;
  }
  .divider {
    position: absolute;
    top: 390px;
    left: 120px;
    width: 810px;
    height: 11px;
    background: var(--lilac-soft);
  }
  .social {
    position: absolute;
    display: flex;
    align-items: center;
    gap: 10px;
    font-size: 20px;
    color: var(--lilac);
  }
  .social-square {
    width: 62px;
    height: 62px;
    border-radius: 8px;
    background: var(--lilac-soft);
  }
  .social-left { left: 26px; top: 400px; }
  .social-right { right: 26px; bottom: 22px; flex-direction: row-reverse; }
</style>
</head>
<body>
  <div class="business-card">
    <div class="card-face" role="img" aria-label="Deep purple background with a grid of soft translucent polka dots">
      <div class="name-band">Lionel Crowthwick</div>

      <ul class="contact-list">
        <li class="contact-item">
          <svg class="contact-icon" viewBox="0 0 40 40" aria-hidden="true">
            <rect x="4" y="10" width="32" height="21" fill="none" stroke="#cdb6cc" stroke-width="2.5"/>
            <path d="M4 10 L20 23 L36 10" fill="none" stroke="#cdb6cc" stroke-width="2.5"/>
          </svg>
          <span>lionel@lionelcrowthwick.com</span>
        </li>
        <li class="contact-item">
          <svg class="contact-icon" viewBox="0 0 40 40" aria-hidden="true">
            <rect x="11" y="3" width="18" height="34" rx="3" fill="none" stroke="#cdb6cc" stroke-width="2.5"/>
            <rect x="14" y="8" width="12" height="20" fill="#cdb6cc" opacity="0.45"/>
            <circle cx="20" cy="32" r="1.8" fill="#cdb6cc"/>
          </svg>
          <span>0418359026</span>
        </li>
        <li class="contact-item">
          <svg class="contact-icon" viewBox="0 0 40 40" aria-hidden="true">
            <g fill="none" stroke="#cdb6cc" stroke-width="2.2">
              <circle cx="20" cy="20" r="15"/>
              <ellipse cx="20" cy="20" rx="7" ry="15"/>
              <line x1="5" y1="20" x2="35" y2="20"/>
              <line x1="8" y1="12" x2="32" y2="12"/>
              <line x1="8" y1="28" x2="32" y2="28"/>
            </g>
          </svg>
          <span>quietsilverhour.com.au</span>
        </li>
      </ul>

      <div class="divider"></div>

      <div class="social social-left"><span class="social-square"></span><span>Pagewall</span></div>
      <div class="social social-right"><span class="social-square"></span><span>Chirpline</span></div>
    </div>
  </div>
</body>
</html>
```